Tamblin Gardening Fresh New Website

We are looking to create a simple fresh website for our landscaping business. The website should appeal to a 'high end' audience. We deal with a lot of Embassies and affluent clients who have extremely large gardens that are meticulously maintained. The site is about communicating our excellent landscaping and customer service skills and encouraging new clients to reach out and engage us to take care of their gardens.

The website is basically going to be our business card, it will have almost no functionality other than two 'contact us' forms, one for smaller clients and one for more detailed projects.

The website will not have a lot of written content and will have to show photos of beautifully landscaped gardens.

The main logo in black will influence the site, however, we are open to all suggestions.

We are expecting to have the following pages:
Home Page
Services
About Us
Contact Us
Showcase (photo gallery of our work)

We need someone who can code it to wordpress and be available for minor changes over a number of days. They will be simple tweaks.

```html
<!DOCTYPE html>
<html lang="en">
<head>
<meta charset="utf-8">
<title>Tamblin Gardening</title>
<link rel="stylesheet" href="https://fonts.googleapis.com/css2?family=Domine:wght@400;500;600;700&family=Noto+Serif:ital,wght@0,400;0,700;1,400&display=swap">
<style>
  :root{
    --ink:#1b1b1b;
    --dark:#1c1c1c;
    --card:#3d3d3d;
    --white:#ffffff;
    --muted:#c9c9c9;
    --gold-1:#b3842a;
    --gold-2:#e8c45c;
    --gold:#c99a35;
    --text:#2a2a2a;
    --line:rgba(255,255,255,.45);
  }
  *{box-sizing:border-box;margin:0;padding:0}
  html,body{width:1200px;height:4342px;overflow:hidden}
  body{position:relative;background:var(--white);font-family:"Noto Serif",Georgia,serif;color:var(--text)}
  .abs{position:absolute}
  .heading{font-family:"Domine",Georgia,serif;font-weight:500;color:var(--ink);text-transform:uppercase}
  .btn{position:absolute;display:flex;align-items:center;justify-content:center;border-radius:30px;
       background:linear-gradient(90deg,var(--gold-1),var(--gold-2) 55%,var(--gold-1));
       font-family:"Domine",Georgia,serif;font-weight:700;color:#2a1f08;text-transform:uppercase;font-size:15px;letter-spacing:.3px;white-space:nowrap}

  /* Hero */
  .hero{position:absolute;left:0;top:0;width:1200px;height:674px;overflow:hidden}
  .hero-photo{position:absolute;inset:0;background:
      radial-gradient(ellipse 380px 520px at 900px 380px,#2f6b4f 0%,transparent 70%),
      radial-gradient(ellipse 300px 300px at 760px 420px,#8a6a55 0%,transparent 70%),
      linear-gradient(100deg,#1d3413 0%,#355a22 35%,#3d6a2c 55%,#2c4f3a 75%,#1f3d33 100%)}
  .hero-shade{position:absolute;inset:0;background:linear-gradient(180deg,rgba(0,0,0,.35),rgba(0,0,0,.15) 40%,rgba(0,0,0,.3))}
  .brand{position:absolute;left:118px;top:84px;width:170px;text-align:center;color:var(--white);font-family:"Noto Serif",Georgia,serif;font-weight:400}
  .brand .name{font-size:20px;letter-spacing:7px;display:block}
  .brand .sub{font-size:10px;letter-spacing:5px;display:block;margin-top:4px}
  .brand-dot{position:absolute;left:185px;top:22px;width:34px;height:34px;border:1.5px solid var(--white);border-radius:50%}
  .topbar{position:absolute;top:21px;font-size:14px;color:var(--white);white-space:nowrap}
  .topbar-line{position:absolute;left:324px;top:64px;width:764px;height:1px;background:var(--line)}
  .nav{position:absolute;top:100px;left:325px;font-size:14px;color:var(--white);text-transform:uppercase}
  .nav span{position:absolute;white-space:nowrap}
  .hero-title{position:absolute;left:0;width:1200px;top:278px;text-align:center;color:var(--white);
      font-family:"Domine",Georgia,serif;font-weight:500;font-size:40px;letter-spacing:5px;line-height:50px}

  /* About */
  .about-photo{position:absolute;left:158px;top:786px;width:358px;height:358px;border-radius:50%;
      background:radial-gradient(circle at 45% 35%,#8aa05a 0%,#5a6e35 35%,#3c2f22 70%,#2a2018 100%)}
  .about-ring{position:absolute;left:150px;top:778px;width:374px;height:374px;border-radius:50%;border:2px solid #f1cf4a}
  .about-title{left:558px;top:806px;font-size:35px;line-height:42px}
  .about-copy{left:558px;top:908px;width:472px;font-size:16px;line-height:26.3px;color:#222}

  /* Services */
  .services{position:absolute;left:0;top:1236px;width:1200px;height:688px;background:var(--dark)}
  .section-title{position:absolute;left:0;width:1200px;text-align:center;font-size:35px}
  .service-card{position:absolute;top:164px;width:294px;height:354px;background:var(--card)}
  .service-photo{height:207px}
  .service-name{position:absolute;left:25px;top:228px;font-family:"Domine",Georgia,serif;font-weight:700;font-size:19px;color:var(--white)}
  .service-desc{position:absolute;left:26px;top:263px;font-size:14px;line-height:18px;color:var(--muted)}
  .service-arrow{position:absolute;left:236px;top:302px}

  .tile{position:absolute}

  /* Testimonials */
  .testimonial{position:absolute;left:209px;top:2945px;width:792px;height:304px;background:var(--white);box-shadow:0 2px 18px rgba(0,0,0,.08)}
  .avatar{position:absolute;left:545px;top:2914px;width:120px;height:120px;border-radius:50%;
      background:radial-gradient(circle at 50% 40%,#b89a7e,#6a7a52 70%,#3f4a34)}
  .reviewer{position:absolute;left:0;width:1200px;top:3052px;text-align:center;font-family:"Domine",Georgia,serif;font-weight:700;font-size:16px;color:#333;letter-spacing:.5px}
  .quote{position:absolute;left:262px;width:686px;top:3087px;text-align:center;font-style:italic;font-size:16.5px;line-height:22.5px;color:#444}
  .stars{position:absolute;left:536px;top:3195px}

  /* Contact */
  .contact{position:absolute;left:0;top:3356px;width:1200px;height:570px;overflow:hidden;
      background:linear-gradient(180deg,#3b3c38 0%,#383a33 45%,#2e312a 100%)}
  .contact-title{position:absolute;left:126px;width:500px;top:86px;text-align:center;font-family:"Domine",Georgia,serif;font-weight:500;font-size:34px;color:var(--white)}
  .field{position:absolute;background:var(--white);border-radius:4px;font-family:"Domine",Georgia,serif;font-weight:600;font-size:14px;color:#333;padding:14px 11px}
  .submit{border-radius:4px;font-size:17px}

  /* Footer */
  .footer{position:absolute;left:0;top:3926px;width:1200px;height:416px;background:#1e1e1e;color:var(--white)}
  .foot-head{position:absolute;top:60px;font-family:"Domine",Georgia,serif;font-weight:500;font-size:22px}
  .foot-rule{position:absolute;top:105px;width:62px;height:1.5px;background:var(--white)}
  .foot-list{position:absolute;top:130px;list-style:none;font-size:15px;line-height:23.5px}
  .foot-brand{position:absolute;left:473px;top:160px;width:300px;text-align:center;color:var(--gold);font-family:"Noto Serif",Georgia,serif;font-weight:400}
  .foot-brand .name{display:block;font-size:28px;letter-spacing:12px}
  .foot-brand .sub{display:block;font-size:15px;letter-spacing:9px;margin-top:6px}
  .foot-dot{position:absolute;left:599px;top:86px;width:48px;height:48px;border:2px solid var(--gold);border-radius:50%}
  .foot-contact{position:absolute;left:842px;font-size:15px;line-height:18px;white-space:nowrap}
  .foot-divider{position:absolute;left:113px;top:292px;width:947px;height:1px;background:#444}
  .copyright{position:absolute;left:0;width:1200px;top:322px;text-align:center;font-size:15px}
</style>
</head>
<body>

<header class="hero">
  <div class="hero-photo" role="img" aria-label="Gardener in green overalls trimming a hedge with a hedge trimmer"></div>
  <div class="hero-shade"></div>
  <div class="brand-dot"></div>
  <div class="brand"><span class="name">TAMBLIN</span><span class="sub">GARDENING</span></div>
  <div class="topbar" style="left:566px">Mon - Fri: 9:00 - 17:00 / Closed on weekends</div>
  <div class="topbar" style="left:941px">CALL: 212 555 0147</div>
  <div class="topbar-line"></div>
  <nav class="nav">
    <span style="left:0">Home</span>
    <span style="left:95px">Services</span>
    <span style="left:217px">About Us</span>
    <span style="left:346px">Contact Us</span>
    <span style="left:486px">Showcase</span>
  </nav>
  <div class="btn" style="left:931px;top:85px;width:157px;height:51px;font-size:15px;text-transform:none">Get a Quote</div>
  <h1 class="hero-title">WELCOME TO<br>TAMBLIN GARDENING</h1>
  <div class="btn" style="left:495px;top:406px;width:210px;height:50px">Request a Quote</div>
</header>

<section class="about">
  <div class="about-ring"></div>
  <div class="about-photo" role="img" aria-label="Hands planting lettuce seedlings in soil beside garden tools"></div>
  <h2 class="heading abs about-title">About<br>Tamblin Gardening</h2>
  <p class="abs about-copy">Lorem ipsum dolor sit amet, consectetur adipiscing elit, sed do eiusmod tempor incididunt ut labore et dolore magna aliqua. Quis ipsum suspendisse ultrices gravida. Risus commodo viverra maecenas accumsan lacus vel facilisis. Lorem ipsum dolor sit amet, consectetur adi piscing elit, sed do eiusmod tempor incididunt ut lab ore et dolore magna aliqua. Quis ipsum suspendisse ultrices gravida.</p>
</section>

<section class="services">
  <h2 class="heading section-title" style="top:86px;color:var(--white)">Our Services</h2>

  <article class="service-card" style="left:126px">
    <div class="service-photo" role="img" aria-label="Hedge being trimmed with a hedge cutter" style="background:linear-gradient(135deg,#5d8a2a,#3f6a1c 55%,#86a845)"></div>
    <h3 class="service-name">Service Name1</h3>
    <p class="service-desc">Lorem ipsum dolor sitm<br>onsectetur adipiscin.</p>
    <svg class="service-arrow" width="40" height="28" viewBox="0 0 40 28"><path d="M14 2 L26 14 L14 26 L2 14 Z" fill="none" stroke="var(--gold)" stroke-width="2"/><path d="M10 14 H37 M30 8 L37 14 L30 20" fill="none" stroke="var(--gold)" stroke-width="2"/></svg>
  </article>

  <article class="service-card" style="left:453px">
    <div class="service-photo" role="img" aria-label="Green lawn mower on a freshly cut lawn" style="background:linear-gradient(180deg,#b9c79a,#6f9a3a 45%,#3d6d1f)"></div>
    <h3 class="service-name">Service Name 2</h3>
    <p class="service-desc">Lorem ipsum dolor sitm<br>onsectetur adipiscin.</p>
    <svg class="service-arrow" width="40" height="28" viewBox="0 0 40 28"><path d="M14 2 L26 14 L14 26 L2 14 Z" fill="none" stroke="var(--gold)" stroke-width="2"/><path d="M10 14 H37 M30 8 L37 14 L30 20" fill="none" stroke="var(--gold)" stroke-width="2"/></svg>
  </article>

  <article class="service-card" style="left:777px">
    <div class="service-photo" role="img" aria-label="Gardener in orange planting flowers in a garden bed" style="background:linear-gradient(135deg,#4f6f2c,#7a8e3e 45%,#b56a36 65%,#5a7a2d)"></div>
    <h3 class="service-name">Service Name 3</h3>
    <p class="service-desc">Lorem ipsum dolor sitm<br>onsectetur adipiscin.</p>
    <svg class="service-arrow" width="40" height="28" viewBox="0 0 40 28"><path d="M14 2 L26 14 L14 26 L2 14 Z" fill="none" stroke="var(--gold)" stroke-width="2"/><path d="M10 14 H37 M30 8 L37 14 L30 20" fill="none" stroke="var(--gold)" stroke-width="2"/></svg>
  </article>

  <div class="btn" style="left:492px;top:560px;width:216px;height:49px">View All Services</div>
</section>

<section class="gallery">
  <h2 class="heading section-title" style="top:2030px">Our Gallery</h2>
  <div class="tile" role="img" aria-label="Potted plants and daisies in warm sunlight" style="left:126px;top:2111px;width:304px;height:267px;background:linear-gradient(135deg,#3a4a14,#8a8a30 45%,#c9a15a 70%,#5b4522)"></div>
  <div class="tile" role="img" aria-label="Neatly trimmed hedge being cut beside a lawn" style="left:448px;top:2111px;width:302px;height:267px;background:linear-gradient(180deg,#2f4a1c,#4f7a2a 50%,#8fb04a)"></div>
  <div class="tile" role="img" aria-label="Gravel path with wooden steps through shrubs" style="left:768px;top:2111px;width:304px;height:267px;background:linear-gradient(160deg,#3d5c2a,#7e9a4a 40%,#b0aaa4 65%,#8a6a44)"></div>
  <div class="tile" role="img" aria-label="Gardener planting pink flowers in a bed, seen from above" style="left:126px;top:2394px;width:465px;height:267px;background:linear-gradient(120deg,#5a5040,#2f4a2a 40%,#4a6a3a 65%,#2f5a48)"></div>
  <div class="tile" role="img" aria-label="Colourful flower garden with red and purple blooms" style="left:607px;top:2394px;width:465px;height:267px;background:linear-gradient(135deg,#3d5a25,#a8385a 35%,#7a4a9a 55%,#c8b88a 80%,#4e6a2e)"></div>
  <div class="btn" style="left:495px;top:2706px;width:210px;height:54px">View Our Works</div>
</section>

<section class="testimonials">
  <h2 class="heading section-title" style="top:2832px;font-size:32px">Client Testimonials</h2>
  <div class="testimonial"></div>
  <div class="avatar" role="img" aria-label="Portrait of a client working in a garden"></div>
  <p class="reviewer">MAREN T</p>
  <p class="quote">Lorem ipsum dolor sit ameconsectetur adipiscing elitse do eiusmod tempor idnt ut labore et dolore mag na aliquaLorem ipsum dolor sit ameconsectetur adipiscing elitse do eiusmod tempor incid idnt ut labore et dolore mag na aliqua. Quis ipsum suspen disse ultrices gravida. is ipsum suspen ds gravida.</p>
  <svg class="stars" width="136" height="26" viewBox="0 0 136 26">
    <defs><path id="star" d="M13 1 L16.5 9 L25 9.6 L18.5 15 L20.6 23.5 L13 19 L5.4 23.5 L7.5 15 L1 9.6 L9.5 9 Z"/></defs>
    <use href="#star" x="0" fill="var(--gold)"/><use href="#star" x="27" fill="var(--gold)"/><use href="#star" x="54" fill="var(--gold)"/><use href="#star" x="81" fill="var(--gold)"/><use href="#star" x="108" fill="var(--gold)"/>
  </svg>
  <svg class="abs" style="left:150px;top:3090px" width="14" height="22" viewBox="0 0 14 22"><path d="M11 2 L3 11 L11 20" fill="none" stroke="#888" stroke-width="2.5"/></svg>
  <svg class="abs" style="left:1036px;top:3090px" width="14" height="22" viewBox="0 0 14 22"><path d="M3 2 L11 11 L3 20" fill="none" stroke="#888" stroke-width="2.5"/></svg>
</section>

<section class="contact">
  <svg class="abs" style="left:0;top:0" width="1200" height="570" viewBox="0 0 1200 570" role="img" aria-label="Garden shrubs and tall grasses lit by a warm sunset">
    <defs>
      <linearGradient id="sunset" x1="0" y1="0" x2="1" y2="1">
        <stop offset="0" stop-color="#4a5a30"/>
        <stop offset=".4" stop-color="#5e6a28"/>
        <stop offset=".65" stop-color="#8a8424"/>
        <stop offset="1" stop-color="#34461e"/>
      </linearGradient>
      <radialGradient id="glow" cx=".9" cy=".08" r=".3">
        <stop offset="0" stop-color="#f0c85a" stop-opacity=".8"/>
        <stop offset="1" stop-color="#f0c85a" stop-opacity="0"/>
      </radialGradient>
    </defs>
    <path d="M790 0 H1200 V570 H770 C720 480 695 380 698 270 C702 160 740 70 790 0 Z" fill="url(#sunset)"/>
    <path d="M790 0 H1200 V570 H770 C720 480 695 380 698 270 C702 160 740 70 790 0 Z" fill="url(#glow)"/>
  </svg>
  <h2 class="contact-title">CONTACT US</h2>
  <div class="field" style="left:126px;top:157px;width:243px;height:46px">Name:</div>
  <div class="field" style="left:382px;top:157px;width:243px;height:46px">Email:</div>
  <div class="field" style="left:126px;top:220px;width:243px;height:46px">Phone:</div>
  <div class="field" style="left:382px;top:220px;width:243px;height:46px">Subject:</div>
  <div class="field" style="left:126px;top:284px;width:499px;height:126px">Message:</div>
  <div class="btn submit" style="left:293px;top:427px;width:165px;height:47px">Submit Now</div>
</section>

<footer class="footer">
  <h3 class="foot-head" style="left:202px">MENU</h3>
  <div class="foot-rule" style="left:202px"></div>
  <ul class="foot-list" style="left:204px"><li>Home</li><li>About us</li><li>Services</li><li>Contact</li><li>Gallery</li></ul>

  <h3 class="foot-head" style="left:347px">LINS</h3>
  <div class="foot-rule" style="left:347px"></div>
  <ul class="foot-list" style="left:348px"><li>Links name 1</li><li>Links name 2</li><li>Links name 3</li><li>Links name 4</li></ul>

  <div class="foot-dot"></div>
  <div class="foot-brand"><span class="name">TAMBLIN</span><span class="sub">GARDENING</span></div>

  <h3 class="foot-head" style="left:810px">CONTACT</h3>
  <div class="foot-rule" style="left:812px"></div>
  <svg class="abs" style="left:818px;top:136px" width="14" height="18" viewBox="0 0 14 18"><path d="M7 1 C3.5 1 1 3.6 1 7 C1 11 7 17 7 17 C7 17 13 11 13 7 C13 3.6 10.5 1 7 1 Z" fill="#fff"/><circle cx="7" cy="7" r="2.3" fill="#1e1e1e"/></svg>
  <p class="foot-contact" style="top:136px">Fernhill Road 18 LJD<br>dumy numers 463.</p>
  <svg class="abs" style="left:818px;top:186px" width="15" height="15" viewBox="0 0 24 24"><path d="M6.6 10.8c1.4 2.8 3.8 5.1 6.6 6.6l2.2-2.2c.3-.3.7-.4 1-.2 1.1.4 2.3.6 3.6.6.6 0 1 .4 1 1V20c0 .6-.4 1-1 1C10.6 21 3 13.4 3 4c0-.6.4-1 1-1h3.5c.6 0 1 .4 1 1 0 1.3.2 2.5.6 3.6.1.3 0 .7-.2 1l-2.3 2.2z" fill="#fff"/></svg>
  <p class="foot-contact" style="top:184px">Phone: 23 555 0192</p>
  <svg class="abs" style="left:818px;top:226px" width="16" height="12" viewBox="0 0 16 12"><rect x="0" y="0" width="16" height="12" rx="1" fill="#fff"/><path d="M1 1 L8 7 L15 1" fill="none" stroke="#1e1e1e" stroke-width="1.5"/></svg>
  <p class="foot-contact" style="top:222px;font-size:14px">Email:hello@tamblingardens.example</p>

  <div class="foot-divider"></div>
  <p class="copyright">Copyright © 2024&nbsp; All Rights Reserved.</p>
</footer>

</body>
</html>
```